Flyer or Info graphic required -for journey map/flow chart

I would like a info graphic designed around the Australian home buying process. explaining all the steps along the way and how it a fits together from the start all the way to settlement and when you pick up the keys.

i want it to be clear and simple. there is quite a lot of words and so the design needs to be simple so they can take it all in.
I have attached an example of one i have seen to give you an idea of what i am thinking as well as the required words

Target Market(s)

25-35 year old first time home buyers

Industry/Entity Type

Financial Service

Font styles to use
Sans Serif

Colors
0355a3

Requirements
Must have
• the word document attached called "start" has the steps i want in my document.
• there is also a hand drawn picture (untitled document) with a portion in yellow, this reflects a certain stage of the process called "cooling off" and it needs to be highlighted as one stage.
• there are also days mentioned on this document so readers understand how long things take
Nice to have
• Logo and Web Address & corporate colours

```html
<!DOCTYPE html>
<html lang="en">
<head>
<meta charset="utf-8">
<title>Your Home Buying Journey – Keystone Home Loans</title>
<link rel="stylesheet" href="https://fonts.googleapis.com/css2?family=Open+Sans:wght@400;600;700&family=Source+Sans+3:wght@400;600&family=Roboto+Condensed:wght@700&display=swap">
<style>
:root{
  --blue:#1c9fe3;
  --blue-deep:#0a87cf;
  --blue-runner:#45b9ef;
  --brand:#0355a3;
  --amber:#f9ab1c;
  --amber-line:#f7b733;
  --step-grey:#c4c4c4;
  --stair-grey:#ebebeb;
  --ink:#2b2b2b;
  --white:#ffffff;
}
*{box-sizing:border-box;margin:0;padding:0}
html,body{width:1200px;height:877px;overflow:hidden;background:var(--white)}
.canvas{width:1200px;height:877px;overflow:hidden;position:relative}
.board{position:absolute;left:0;top:0;width:1500px;height:1096px;transform:scale(.8);transform-origin:0 0;font-family:"Open Sans",sans-serif;color:var(--ink)}
.abs{position:absolute}
.connectors,.stair-shape{position:absolute;left:0;top:0;width:1500px;height:1096px}
.scene{left:565px;top:35px;width:355px;height:177px;border-bottom:2px solid #ccc;background:linear-gradient(180deg,#ffffff 0%,#fbe3d2 45%,#f0a06c 100%)}
.step{position:absolute;display:flex;align-items:center;justify-content:center;text-align:center;color:var(--white);font-weight:700;line-height:1.1;white-space:nowrap}
.step-side{position:absolute;background:var(--step-grey)}
.step.blue{background:var(--blue)}
.step.amber{background:var(--amber)}
.step small{display:block;font-size:10px}
.tag{position:absolute;background:var(--step-grey);color:var(--brand);font-family:"Roboto Condensed",sans-serif;font-weight:700;text-align:center;line-height:1}
.note{position:absolute;background:var(--white);border:2px solid var(--blue);border-radius:4px;font-family:"Source Sans 3",sans-serif;font-size:13px;line-height:1.18;padding:4px 8px}
.note.amber{border-color:var(--amber-line)}
.note p{margin:0}
.note .ind{padding-left:15px;text-indent:-15px}
.note .ind2{padding-left:28px}
.day{position:absolute;border-radius:50%;background:var(--white);border:2px solid var(--blue);display:flex;flex-direction:column;align-items:center;justify-content:center;font-family:"Roboto Condensed",sans-serif;font-weight:700;color:var(--brand);line-height:.95}
.day.amber{border-color:var(--amber-line);color:var(--amber)}
.party{left:131px;top:346px;font-family:"Roboto Condensed",sans-serif;font-weight:700;font-size:20px;color:var(--blue-deep)}
.brand-name{left:34px;top:1028px;font-family:"Roboto Condensed",sans-serif;font-weight:700;font-size:28px;color:var(--brand);display:flex;align-items:center;gap:8px;line-height:1}
.brand-name .mark{width:16px;height:16px;background:var(--brand)}
.web{right:16px;top:1066px;font-size:21px;font-weight:600;color:var(--brand)}
</style>
</head>
<body>
<main class="canvas">
<div class="board">

  <svg class="stair-shape" viewBox="0 0 1500 1096" aria-hidden="true">
    <polygon points="655,212 840,212 1062,975 438,975" fill="var(--stair-grey)"/>
    <polygon points="688,212 804,212 960,975 540,975" fill="var(--blue-runner)"/>
  </svg>

  <div class="abs scene" role="img" aria-label="Illustration of a family and a broker standing beside their new house at the top of the stairs"></div>

  <div class="step-side" style="left:668px;top:215px;width:154px;height:27px"></div>
  <div class="step blue" style="left:688px;top:215px;width:116px;height:27px;font-size:9px">1st payment is Due</div>

  <div class="step-side" style="left:664px;top:245px;width:162px;height:25px"></div>
  <div class="step blue" style="left:682px;top:245px;width:128px;height:25px;font-size:8px">Internet banking &amp;<br>account set up</div>

  <div class="step-side" style="left:660px;top:275px;width:172px;height:25px"></div>
  <div class="step blue" style="left:680px;top:275px;width:132px;height:25px;font-size:10px">Settlement</div>
  <div class="tag" style="left:814px;top:277px;width:18px;height:21px;font-size:8px">Day<br>42</div>

  <div class="step-side" style="left:655px;top:304px;width:182px;height:24px"></div>
  <div class="step blue" style="left:677px;top:304px;width:139px;height:24px;font-size:10px">Cheque Directions</div>

  <div class="step-side" style="left:648px;top:334px;width:198px;height:26px"></div>
  <div class="step blue" style="left:672px;top:334px;width:148px;height:26px;font-size:10px">Settlement is Booked</div>
  <div class="tag" style="left:648px;top:336px;width:22px;height:22px;font-size:8px">Party<br>Time</div>
  <div class="tag" style="left:822px;top:336px;width:24px;height:22px;font-size:8px">Day<br>40</div>

  <div class="step-side" style="left:640px;top:368px;width:212px;height:27px"></div>
  <div class="step blue" style="left:667px;top:368px;width:159px;height:27px;font-size:8px">Lender Reviews Documents<br>and is “ready to book settlement”</div>

  <div class="step-side" style="left:632px;top:405px;width:228px;height:23px"></div>
  <div class="step blue" style="left:662px;top:405px;width:168px;height:23px;font-size:9.5px">Lender Prepares Loan Documents</div>

  <div class="step-side" style="left:622px;top:437px;width:248px;height:22px"></div>
  <div class="step amber" style="left:656px;top:437px;width:180px;height:22px;font-size:11px">Cooling Off Expires</div>
  <div class="tag" style="left:838px;top:440px;width:32px;height:18px;font-size:12px;line-height:18px">Day 5</div>

  <div class="step-side" style="left:612px;top:469px;width:268px;height:26px"></div>
  <div class="step amber" style="left:650px;top:469px;width:192px;height:26px;font-size:11px">Formal Approval</div>

  <div class="step-side" style="left:600px;top:508px;width:293px;height:28px"></div>
  <div class="step amber" style="left:642px;top:508px;width:208px;height:28px;font-size:12px">Strata Report / Building Report</div>

  <div class="step-side" style="left:590px;top:548px;width:315px;height:28px"></div>
  <div class="step amber" style="left:636px;top:548px;width:220px;height:28px;font-size:10.5px">Final Instructions to your Lender/bank</div>

  <div class="step-side" style="left:577px;top:585px;width:338px;height:29px"></div>
  <div class="step amber" style="left:628px;top:585px;width:238px;height:29px;font-size:16px">Offer Accepted</div>
  <div class="tag" style="left:868px;top:588px;width:47px;height:24px;font-size:20px;line-height:24px">Day 1</div>

  <div class="step-side" style="left:563px;top:628px;width:367px;height:31px"></div>
  <div class="step blue" style="left:620px;top:628px;width:256px;height:31px;font-size:16px">Make an offer</div>

  <div class="step-side" style="left:546px;top:672px;width:404px;height:40px"></div>
  <div class="step blue" style="left:612px;top:672px;width:272px;height:40px;font-size:15px;flex-direction:column">You found the Dream Home -<small>Before you make an offer</small></div>

  <div class="step-side" style="left:528px;top:729px;width:442px;height:33px"></div>
  <div class="step blue" style="left:598px;top:729px;width:302px;height:33px;font-size:16px">Time to go shopping</div>

  <div class="step-side" style="left:508px;top:774px;width:480px;height:36px"></div>
  <div class="step blue" style="left:586px;top:774px;width:328px;height:36px;font-size:16px">Appoint your Conveyancer</div>

  <div class="step-side" style="left:488px;top:830px;width:528px;height:39px"></div>
  <div class="step blue" style="left:572px;top:830px;width:356px;height:39px;font-size:17px">Get your Pre-Approval in place</div>

  <div class="step-side" style="left:466px;top:895px;width:570px;height:45px"></div>
  <div class="step blue" style="left:556px;top:895px;width:388px;height:45px;font-size:17px">Time to start “Living Like You Have<br>a Mortgage”</div>

  <div class="step-side" style="left:438px;top:975px;width:624px;height:57px"></div>
  <div class="step blue" style="left:540px;top:975px;width:415px;height:57px;font-size:44px">Start</div>

  <svg class="connectors" viewBox="0 0 1500 1096" aria-hidden="true" fill="none" stroke-width="1.5">
    <g stroke="var(--blue)">
      <polyline points="595,265 630,265 630,228 688,228"/>
      <polyline points="494,335 640,335 640,288 680,288"/>
      <polyline points="598,380 615,380 615,348 648,348"/>
      <polyline points="486,690 612,690"/>
      <polyline points="484,795 586,795"/>
      <polyline points="320,887 320,913 556,913"/>
      <polyline points="810,255 895,255 895,263 978,263"/>
      <polyline points="816,316 880,316 880,350 918,350"/>
      <polyline points="830,416 905,416 905,438 948,438"/>
      <polyline points="876,645 980,645 980,698 1020,698"/>
      <polyline points="1188,828 1188,855 928,855"/>
    </g>
    <g stroke="var(--amber-line)">
      <polyline points="546,430 585,430 585,448 656,448"/>
      <polyline points="514,505 560,505 560,522 642,522"/>
      <polyline points="510,600 628,600"/>
      <polyline points="842,482 920,482 920,505 963,505"/>
      <polyline points="856,566 980,566 980,585 1027,585"/>
    </g>
  </svg>

  <div class="day" style="left:55px;top:233px;width:64px;height:64px;font-size:23px">Day<span>42</span></div>
  <div class="day" style="left:58px;top:352px;width:52px;height:52px;font-size:19px">Day<span>40</span></div>
  <div class="day amber" style="left:124px;top:402px;width:52px;height:52px;font-size:19px">Day<span>5</span></div>
  <div class="day amber" style="left:43px;top:569px;width:68px;height:68px;font-size:24px">Day<span>1</span></div>
  <div class="abs party">Party Time</div>

  <div class="note" style="left:122px;top:228px;width:473px">
    <p class="ind">A.&nbsp; Normally 1 month after settlement</p>
    <p class="ind">B.&nbsp; The Lender often messes this up – Call them to make sure it is set up how YOU want it</p>
    <p class="ind">C.&nbsp; Call them to set up a payment date that suits you – ie the day after your pay</p>
  </div>
  <div class="note" style="left:262px;top:308px;width:232px">
    <p>A. Your Conveyancer will contact you</p>
    <p>B. Pick up the keys for the Estate Agent</p>
    <p>C. Pizza party at your place!!!</p>
  </div>
  <div class="note" style="left:116px;top:368px;width:482px;padding-top:3px;padding-bottom:3px">
    <p>Your Conveyancer will coordinate this with your Lender and the Sellers Conveyancer</p>
  </div>
  <div class="note amber" style="left:180px;top:408px;width:366px;padding:5px 8px 5px 12px">
    <p>Now that you have your Approval and your reports are all ok, Cooling can expire and the Contract becomes “Formal”.</p>
  </div>
  <div class="note amber" style="left:122px;top:477px;width:392px">
    <p class="ind">A.&nbsp; If you are buying a Unit – Talk to your conveyancer and get a strata report done.</p>
    <p class="ind">B.&nbsp; If you are buying a house – you need a “Pest &amp; Building Report”</p>
  </div>
  <div class="note amber" style="left:118px;top:554px;width:392px">
    <p class="ind">A.&nbsp; Get the Contract and price to your Broker –make sure they know your Conveyancers Details.</p>
    <p class="ind">B.&nbsp; Sign the Contract &amp; pay your deposit (‘Normally’ 0.25% of the purchase price)</p>
    <p class="ind">C.&nbsp; Contracts are then “Exchanged” – and Cooling Off starts (normally 5 days)</p>
  </div>
  <div class="note" style="left:118px;top:674px;width:368px">
    <p>A.&nbsp; Have you done your research? Get a Property Profile report</p>
    <p>B.&nbsp; Ask the agent “what happens if my offer is accepted”</p>
  </div>
  <div class="note" style="left:100px;top:765px;width:384px">
    <p class="ind">A. Make sure you understand the Cost (ask them if this includes re-viewing 1 or 2 Contracts in case you miss out on a property)</p>
    <p>B. Ask them – “what do I do once my offer is accepted”</p>
  </div>
  <div class="note" style="left:228px;top:848px;width:187px;text-align:center;padding:4px 4px">
    <p>Idea: get the checklist from www.keystonehomeloans.com.au</p>
  </div>

  <div class="note" style="left:978px;top:244px;width:378px">
    <p>A. This may take your Lender 7-10 days after settlement</p>
    <p>B. But you should be proactive and call them to set everything</p>
  </div>
  <div class="note" style="left:918px;top:306px;width:530px">
    <p class="ind">A.&nbsp; This is where your Conveyancer checks exactly what has been paid, who needs to be paid and where the available money is sitting.</p>
    <p class="ind">B.&nbsp; If you have more savings to contribute they will give you the exact number.</p>
    <p class="ind2">i. please make sure you ask them how to provide the funds. Eg can you transfer it to their Trust Account or do you need a bank cheque?</p>
  </div>
  <div class="note" style="left:948px;top:408px;width:460px">
    <p class="ind">A.&nbsp; Work with your broker to make sure they are correct and you understand all the documents before you sign.</p>
    <p>B.&nbsp; Return the signed documents to the Lender.</p>
  </div>
  <div class="note amber" style="left:963px;top:485px;width:452px">
    <p>A. When the Valuation is back (3 days) the bank will issue the Formal Approval</p>
    <p>B. Your broker will email you a copy and provide one to your Conveyancer</p>
  </div>
  <div class="note amber" style="left:1027px;top:544px;width:408px">
    <p class="ind">A.&nbsp; Now that you have the purchase price - You and your Broker need to finalise the loan amount plus the structure (i.e fixed or variable rates)</p>
    <p>B.&nbsp; Your broker will instruct the Lender to proceed</p>
    <p>C.&nbsp; A Valuation is ordered</p>
  </div>
  <div class="note" style="left:1020px;top:656px;width:417px">
    <p class="ind">A.&nbsp; Remember this is not binding until you sign the contract and pay the deposit, your ‘just’ making an offer.</p>
    <p class="ind">B.&nbsp; Make sure your conveyancer has seen the contract before you sign it Remember – it is possible to also negotiate a smaller deposit (eg 5%)</p>
    <p>C.&nbsp; and longer cooling off period and or a longer Settlement period</p>
  </div>
  <div class="note" style="left:1035px;top:773px;width:305px">
    <p>Make an appointment to talk to your Professional Mortgage Broker to discuss your Lender and Interest rate options and get the Pre-Approval under way</p>
  </div>

  <div class="abs brand-name"><span class="mark"></span>KEYSTONE HOME LOANS</div>
  <div class="abs web">www.keystonehomeloans.com.au</div>

</div>
</main>
</body>
</html>
```